Neukunden-Flyer für Yoga-&Massage
Zielgruppe
Yoga-Leherin, die Yoga nicht nur zur zeitweisen Entspannung vermittelt sondern als Ansatz dauerhafter Entschleunigung, Stressbewältigung und körperlicher Fitness. Thai Yoga Massage arbeitet nicht nur körperlich sondern auch energetisch auch auf der Herzebene.
Zielgruppe:
Jeder, der sich etwas Gutes tun will und seine Selbstheilungskräfte aktivieren und wieder mehr bei sich sein möchte.
Aufgabenstellung
Erstellung eines Flyers mit folgenden Eigenschaften:
• DIN A4 lang - Wickelfalz-Flyer 6-seitig
• Klare Formen und kräftige Farben
• Einprägsam
• Fließend
• CMYK - keine Sonderfarben
• Druckdatenvorlage (PSDs (außen/innen bzw. Druckdatenerstellung Fonts/Pfade
beachten)
Abgabe als offene Datei: PSD, AI bzw. als geschlossene Druckdatei X3 PDF.

```html
<!DOCTYPE html>
<html lang="de">
<head>
<meta charset="utf-8">
<title>Flyer Yoga &amp; Massage – Innenseite</title>
<link rel="stylesheet" href="https://fonts.googleapis.com/css2?family=Roboto:wght@300;400;500;700&display=swap">
<style>
  :root {
    --pink: #e0137f;
    --yellow: #d6cf12;
    --band: #ece98c;
    --ink: #6a6a6a;
    --ink-strong: #6f6f6f;
    --paper: #ffffff;
    --stage: #e9e9e9;
  }
  * { margin: 0; padding: 0; box-sizing: border-box; }
  html, body { width: 1200px; height: 675px; overflow: hidden; background: var(--stage); }
  body { font-family: "Roboto", Arial, sans-serif; color: var(--ink); }

  .flyer {
    position: absolute; left: 150px; top: 17px;
    width: 900px; height: 640px;
    background: var(--paper); overflow: hidden;
  }
  .flyer__band { position: absolute; left: 0; top: 0; width: 900px; height: 130px; }
  .flyer__stones {
    position: absolute; left: 0; top: 470px; width: 900px; height: 170px;
    background: linear-gradient(180deg, rgba(255,255,255,1) 0%, rgba(214,222,228,.55) 30%, #b9c6cf 60%, #dfe7ec 100%);
  }

  .portrait { position: absolute; width: 160px; height: 160px; }
  .portrait--massage { left: 67px; top: 25px; }
  .portrait--yoga { left: 361px; top: 25px; }
  .portrait--coach { left: 672px; top: 25px; }

  .rule { position: absolute; height: 1px; }
  .rule--pink { background: var(--pink); }
  .rule--yellow { background: var(--yellow); }
  .bar { position: absolute; height: 5px; }
  .bar--pink { background: var(--pink); }
  .bar--yellow { background: var(--yellow); }

  .title {
    position: absolute; top: 186px; font-weight: 300; font-size: 30px;
    line-height: 34px; text-align: center; white-space: nowrap;
  }
  .title--pink { color: var(--pink); }
  .title--yellow { color: var(--yellow); }
  .title--gray { color: #777; }

  .text { position: absolute; text-align: center; }
  .text--lead { font-weight: 500; font-size: 12.6px; line-height: 15.7px; color: var(--ink-strong); }
  .text--body { font-weight: 300; font-size: 10.2px; line-height: 12.9px; }
  .text--body-large { font-weight: 300; font-size: 12.4px; line-height: 15.5px; }
  .text--note { font-weight: 500; font-size: 10.2px; line-height: 13px; color: var(--ink-strong); }
  .text--price-head { font-weight: 500; font-size: 18.5px; line-height: 20px; color: #7a7a7a; }
  .text--prices { font-weight: 500; font-size: 12.6px; line-height: 15.5px; color: #7a7a7a; }
</style>
</head>
<body>
<main class="flyer">
  <svg class="flyer__band" viewBox="0 0 900 130" aria-hidden="true">
    <path d="M0 0 H900 V86 C780 40 600 18 440 22 C270 26 110 60 0 114 Z" fill="var(--band)"/>
  </svg>

  <svg class="portrait portrait--massage" viewBox="0 0 160 160" role="img" aria-label="Foto: Thai-Yoga-Massage an der Schulter">
    <circle cx="80" cy="80" r="77" fill="none" stroke="var(--pink)" stroke-width="2" stroke-dasharray="0.1 5" stroke-linecap="round"/>
    <defs><linearGradient id="gMassage" x1="0" y1="0" x2="1" y2="1"><stop offset="0" stop-color="#e9d6c9"/><stop offset="1" stop-color="#b8a69a"/></linearGradient></defs>
    <circle cx="80" cy="82" r="64" fill="#555" opacity=".35"/>
    <circle cx="80" cy="80" r="62" fill="url(#gMassage)" stroke="var(--pink)" stroke-width="5"/>
  </svg>
  <svg class="portrait portrait--yoga" viewBox="0 0 160 160" role="img" aria-label="Foto: Frau in weißer Kleidung in einer Yoga-Haltung">
    <circle cx="80" cy="80" r="77" fill="none" stroke="var(--yellow)" stroke-width="2" stroke-dasharray="0.1 5" stroke-linecap="round"/>
    <defs><radialGradient id="gYoga"><stop offset="0" stop-color="#f4f1ee"/><stop offset="1" stop-color="#ffffff"/></radialGradient></defs>
    <circle cx="80" cy="82" r="64" fill="#555" opacity=".35"/>
    <circle cx="80" cy="80" r="62" fill="url(#gYoga)" stroke="var(--yellow)" stroke-width="5"/>
  </svg>
  <svg class="portrait portrait--coach" viewBox="0 0 160 160" role="img" aria-label="Foto: Frau meditiert vor dem Meer">
    <circle cx="80" cy="80" r="77" fill="none" stroke="var(--pink)" stroke-width="2" stroke-dasharray="0.1 5" stroke-linecap="round"/>
    <defs><linearGradient id="gCoach" x1="0" y1="0" x2="0" y2="1"><stop offset="0" stop-color="#c9dbe6"/><stop offset="1" stop-color="#e9eef2"/></linearGradient></defs>
    <circle cx="80" cy="82" r="64" fill="#555" opacity=".35"/>
    <circle cx="80" cy="80" r="62" fill="url(#gCoach)" stroke="var(--pink)" stroke-width="5"/>
  </svg>

  <div class="flyer__stones" role="img" aria-label="Foto: Steine auf ruhigem Wasser"></div>

  <!-- Thai Yoga Massage -->
  <h2 class="title title--pink" style="left:17px;width:258px;">Thai Yoga Massage</h2>
  <div class="rule rule--pink" style="left:17px;width:258px;top:221px;"></div>
  <p class="text text--lead" style="left:17px;width:258px;top:227px;">Wann haben Sie sich das letzte Mal in<br>Ihrem Körper zuhause gefühlt?</p>
  <p class="text text--body" style="left:17px;width:258px;top:266px;">Thai Yoga Massage ermöglicht tiefe<br>Regeneration. Verspannungen und<br>Energieblockaden werden durch<br>nährende Berührungen wirkungsvoll<br>gelöst. Die Erfahrung bewegt zu<br>werden umfasst Körper, Seele<br>und Geist. Ein Erlebnis, dass noch<br>lange nachwirkt.</p>
  <div class="rule rule--pink" style="left:111px;width:72px;top:373px;"></div>
  <p class="text text--note" style="left:17px;width:258px;top:380px;">Gönnen Sie sich einen ruhigen Raum,<br>Achtsamkeit, Präsenz, Zeit nur für sich.<br>Eine&nbsp; Investition um neue Energie<br>zu tanken.</p>
  <div class="bar bar--pink" style="left:111px;width:72px;top:435px;"></div>
  <p class="text text--price-head" style="left:17px;width:258px;top:445px;">Preise</p>
  <p class="text text--prices" style="left:17px;width:258px;top:465px;">Schnupperpreis 60 min / 45 Euro<br>60 Minuten – 60 Euro<br>90 Minuten – 85 Euro<br>120 Minuten – 110 Euro</p>

  <!-- Yoga -->
  <div class="rule rule--yellow" style="left:313px;width:94px;top:206px;"></div>
  <h2 class="title title--yellow" style="left:407px;width:70px;">Yoga</h2>
  <div class="rule rule--yellow" style="left:477px;width:94px;top:206px;"></div>
  <div class="rule rule--yellow" style="left:313px;width:258px;top:221px;"></div>
  <p class="text text--body" style="left:313px;width:258px;top:227px;">Der Einzelunterricht richtet sich<br>nach Ihren individuellen Zielen und Wünschen. Ihren<br>Fähigkeiten nach, erarbeiten wir<br>ihre ganz persönliche Übungssequenz.<br>Die Atmung ist der Schlüssel zur bewussten<br>Wahrnehmung. Steigerung des körperlichen Wohlbe-<br>findens, Ausgeglichenheit und Widerstandsfähigkeit<br>sind die Folge.</p>
  <div class="rule rule--yellow" style="left:407px;width:72px;top:338px;"></div>
  <p class="text text--note" style="left:313px;width:258px;top:344px;">Jede Stunde endet mit einer 5-minütigen<br>Nackenmassage und anschließender<br>Tiefenentspannung</p>
  <div class="bar bar--yellow" style="left:407px;width:72px;top:438px;"></div>
  <p class="text text--price-head" style="left:313px;width:258px;top:449px;">Preise</p>
  <p class="text text--prices" style="left:313px;width:258px;top:468px;">Schnupperpreis 60 min / 55 Euro<br>60 Minuten – 85 Euro<br>90 Minuten – 110 Euro</p>

  <!-- Coach -->
  <div class="rule rule--pink" style="left:624px;width:85px;top:206px;"></div>
  <h2 class="title title--gray" style="left:709px;width:87px;">Coach</h2>
  <div class="rule rule--pink" style="left:796px;width:86px;top:206px;"></div>
  <div class="rule rule--pink" style="left:624px;width:258px;top:221px;"></div>
  <p class="text text--body-large" style="left:614px;width:278px;top:227px;">Im Coaching lernen Sie mit beruflichen<br>Konflikten und persönlichen Beziehungs-<br>spannungen umzugehen. Ich gebe Ihnen<br>alltagstaugliche Techniken an die Hand<br>um sich für die persönlichen Herausfor-<br>derungen zu stärken und immer wieder<br>tiefe Ruhepole zu finden</p>
  <div class="bar bar--pink" style="left:717px;width:72px;top:346px;"></div>
  <p class="text text--price-head" style="left:624px;width:258px;top:357px;">Preise</p>
  <p class="text text--prices" style="left:624px;width:258px;top:377px;">Schnupperpreis 60 min / 55 Euro<br>60 Minuten – 85 Euro<br>90 Minuten – 110 Euro</p>
</main>
</body>
</html>
```